"The Craft of Patron Care," fourth edition cover design

Later this year, my publisher, Harold Brenton & Co., will issue a fourth, substantially revised edition of "The Craft of Patron Care," following the 2016 publication of the third edition and the second and first versions that were issued earlier.

To distinguish this new edition from previous ones, I need a cover design that visually connects and is consistent with what has preceded it, while signaling this is a new and different, worthy of prospective readers/buyers’ attention.

Attached are three different verbal approaches to the new cover; these are NOT MEANT to serve as actual designs, but rather will give you a sense of how language is to be deployed:

The first emphasizes “ART” as the key visual word in the book title;
The second emphasizes “CLIENT SERVICE” as the key visual words in the book title; and,
The third emphasizes just the word "CLIENT" in the book title.

A top-of-the-page is a pre-head that applies to all three versions:
“6 TIMELESS PRINCIPLES FOR ADVERTISING & MARKETING PRO’s
IN AN AI WORLD"

There's a mid-page sub-head for all three versions:
“THE CLASSIC GUIDE,” followed by
“FOURTH EDITION BY DENNIS HARTWELL

And there's a one-line, bottom-of-the-page designation:
“Foreword by Pam Kettering, Global Executive Creative Director, Bluefinch"

The pallette for the previously published third edition was black with red as an accent color on a field of white; I've attached a sample for reference, so you can see how it was executed. For this new fourth edition, I'd like to change the accent color from red to either Wedgewood blue, or British racing green, or an alternative that is assertive and color saturated -- think of primary colors -- that contrast sufficiently with the base of black. As an alternative, you can consider a cover that used either Wedgewood blue, British racing green, or another possibility as a full-bleed field, with copy content either revered out or surprinted.

Lastly, while the new cover largely is meant to be typographically driven, if you can come up with a visual metaphor that illustrates and builds on the book's title, that would be very helpful. By way of reference, the third edition's book cover attempted to do this by introducing a visual element at the end of the book's title that's meant to represent an artist's paint splatter (although I admit it didn't work as well as it should).

Target Market(s)

Prospective purchasers of the book who might discover copies at a bookstore, but more likely will encounter it through online distributors such as Vendora, Fitch & Marlow, and Tindle’s.

Industry/Entity Type

Advertising and marketing

Font styles to use
Serif
Sans Serif
Other font styles liked:
• A mix of serif and san-serif typefaces is okay. for the examples I shared, I relieid on "Arial Rounded Bold" but you need not be weeded to this. If you opt to mix in a serif font, I am partial to Cambria as a typeface.

Requirements
Must have
• To achieve the goal of being “connected with but distinct” from previous editions, the new cover should be:  Largely typographic, but displaying a color palette different from the previous editions’ black-plus-red-accent on a canvas of white.  Any new accent color selected for use should be vibrant, strong, and highly saturated; think “British racing green,” “Wedgewood blue,” or their equivalents.  In addition to a powerful, “billboard” approach to type and color, consider other visual metaphors that are likely to engage the readers. The winning cover design will stand out from other books, while connecting with the previously published third edition.
Nice to have
• If you can find way to illustrate the book's title through a visual metaphor, that would be ideal.a
Should not have
• Anything that is frivolous or non-sensical

```html
<!DOCTYPE html>
<html lang="en">
<head>
<meta charset="utf-8">
<title>The Craft of Patron Care — Fourth Edition Cover</title>
<link rel="stylesheet" href="https://fonts.googleapis.com/css2?family=EB+Garamond:wght@400;500&family=Inter+Tight:wght@600;800&display=swap">
<style>
  :root {
    --stage: #c4c0ba;
    --racing-green: #1f4039;
    --accent-red: #cf3a40;
    --ivory: #e9e5dc;
    --rule: rgba(233, 229, 220, 0.35);
  }
  * { margin: 0; padding: 0; box-sizing: border-box; }
  html, body {
    width: 1200px;
    height: 1050px;
    overflow: hidden;
    background: var(--stage);
  }
  .canvas {
    position: relative;
    width: 1200px;
    height: 1050px;
  }
  .cover {
    position: absolute;
    left: 300px;
    top: 45px;
    width: 600px;
    height: 960px;
    background: var(--racing-green);
    text-align: center;
    color: var(--ivory);
  }
  .prehead {
    position: absolute;
    top: 62px;
    left: 0;
    right: 0;
    font-family: "EB Garamond", Georgia, serif;
    font-size: 16px;
    line-height: 26px;
    letter-spacing: 0.01em;
  }
  .rule {
    position: absolute;
    left: 50%;
    width: 56px;
    height: 1px;
    margin-left: -28px;
    background: var(--rule);
  }
  .rule--top { top: 128px; }
  .rule--mid { top: 716px; }
  .title {
    position: absolute;
    top: 290px;
    left: 0;
    right: 0;
    font-family: "Inter Tight", Arial, sans-serif;
    font-weight: 800;
    color: var(--accent-red);
    text-transform: uppercase;
    letter-spacing: -0.02em;
  }
  .title__lead {
    display: block;
    font-size: 34px;
    line-height: 40px;
    font-weight: 600;
  }
  .title__word {
    display: block;
    line-height: 0.92;
  }
  .title__word--first { font-size: 112px; margin-top: 6px; }
  .title__word--second { font-size: 132px; }
  .edition {
    position: absolute;
    top: 630px;
    left: 0;
    right: 0;
    font-family: "Inter Tight", Arial, sans-serif;
    font-weight: 600;
    color: var(--accent-red);
  }
  .edition__number {
    display: block;
    font-size: 36px;
    line-height: 40px;
  }
  .edition__label {
    display: block;
    margin-top: 12px;
    font-size: 15px;
    letter-spacing: 0.01em;
  }
  .credits {
    position: absolute;
    top: 832px;
    left: 0;
    right: 0;
    font-family: "EB Garamond", Georgia, serif;
  }
  .credits__author {
    display: block;
    font-size: 15px;
    letter-spacing: 0.02em;
  }
  .credits__foreword {
    display: block;
    margin-top: 14px;
    font-size: 12px;
    line-height: 17px;
    letter-spacing: 0.01em;
  }
</style>
</head>
<body>
  <main class="canvas">
    <section class="cover" aria-label="Book cover: The Craft of Patron Care, fourth edition">
      <p class="prehead">SIX TIMELESS PRINCIPLES FOR ADVERTISING &amp; MARKETING PRO’s<br>IN AN AI WORLD</p>
      <span class="rule rule--top"></span>

      <h1 class="title">
        <span class="title__lead">The Craft of</span>
        <span class="title__word title__word--first">Patron</span>
        <span class="title__word title__word--second">Care</span>
      </h1>

      <p class="edition">
        <span class="edition__number">04</span>
        <span class="edition__label">THE CLASSIC GUIDE</span>
      </p>
      <span class="rule rule--mid"></span>

      <p class="credits">
        <span class="credits__author">DENNIS HARTWELL</span>
        <span class="credits__foreword">FOREWORD BY PAM KETTERING, GLOBAL EXECUTIVE<br>CREATIVE DIRECTOR, BLUEFINCH</span>
      </p>
    </section>
  </main>
</body>
</html>
```